Salt Water Delivery Company Business Card Design

We are a company that delivers natural saltwater (from the ocean) to aquarium companies, restaurants and home marine tanks. I would like a new business card to suit.

Must include Name, company name, abn, contact number and website as well as logo (see attached).

Looking for a design that stands out, has a clean but unique appearance.

Double and single sided entries welcome

Industry/Entity Type

Business

Requirements
Must have
• Logo

```html
<!DOCTYPE html>
<html lang="en">
<head>
<meta charset="utf-8">
<title>Brine Run — Business Card</title>
<link rel="stylesheet" href="https://fonts.googleapis.com/css2?family=Mulish:wght@400;600;800&display=swap">
<style>
  :root {
    --page-bg: #e4e6e8;
    --brand-blue: #1a8ccd;
    --brand-blue-deep: #137bb8;
    --brand-blue-light: #3aa6e0;
    --card-white: #ffffff;
    --card-grey: #eef0f1;
    --ink: #3a3d40;
    --rule: #55585b;
  }
  * { margin: 0; padding: 0; box-sizing: border-box; }
  html, body {
    width: 1200px; height: 900px; overflow: hidden;
    background: var(--page-bg);
    font-family: "Mulish", sans-serif;
  }
  .canvas {
    width: 1200px; height: 900px;
    display: flex; flex-direction: column; align-items: center; justify-content: center;
    gap: 40px;
  }
  .card {
    width: 700px; height: 400px; position: relative; overflow: hidden;
    box-shadow: 0 6px 18px rgba(0,0,0,0.18);
  }

  /* Back side */
  .card-back {
    background: radial-gradient(ellipse at 55% 40%, var(--brand-blue-light), var(--brand-blue-deep) 85%);
    color: var(--card-white);
    display: flex; flex-direction: column; align-items: center; justify-content: center;
  }
  .card-back .brand { display: flex; align-items: center; gap: 14px; }
  .card-back .brand-name { font-size: 58px; font-weight: 800; color: var(--card-white); letter-spacing: 0.5px; }
  .card-back .brand-dot { width: 22px; height: 22px; border-radius: 50%; background: var(--card-white); }
  .card-back .website { margin-top: 46px; font-size: 17px; letter-spacing: 0.6px; opacity: 0.9; }

  /* Front side */
  .card-front {
    background: linear-gradient(160deg, var(--card-white) 40%, var(--card-grey));
    color: var(--ink);
  }
  .card-front .edge {
    position: absolute; left: 0; right: 0; bottom: 0; height: 10px; background: var(--brand-blue);
  }
  .card-front .brand { position: absolute; left: 44px; top: 52px; display: flex; align-items: center; gap: 10px; }
  .card-front .brand-name { font-size: 40px; font-weight: 800; color: var(--brand-blue); }
  .card-front .brand-dot { width: 16px; height: 16px; border-radius: 50%; background: var(--brand-blue); }
  .card-front .person { position: absolute; right: 48px; top: 56px; text-align: right; }
  .card-front .person-name { font-size: 24px; font-weight: 400; letter-spacing: 0.5px; }
  .card-front .person-role { font-size: 17px; color: var(--brand-blue); letter-spacing: 0.6px; }
  .card-front .rule { position: absolute; height: 1.5px; background: var(--rule); }
  .card-front .rule-top { left: 310px; right: 48px; top: 126px; }
  .card-front .rule-bottom { left: 44px; right: 300px; top: 252px; }
  .card-front .contact { position: absolute; left: 44px; top: 270px; list-style: none; }
  .card-front .contact li { display: flex; align-items: center; gap: 12px; font-size: 20px; letter-spacing: 0.8px; line-height: 32px; }
  .card-front .contact svg { width: 16px; height: 16px; fill: var(--brand-blue); flex: none; }
  .card-front .abn { color: var(--brand-blue); margin-top: 4px; }
  .card-front .front-website { position: absolute; right: 48px; top: 214px; font-size: 19px; letter-spacing: 0.8px; }
</style>
</head>
<body>
<main class="canvas">
  <section class="card card-back" aria-label="Card back">
    <div class="brand">
      <span class="brand-dot"></span>
      <span class="brand-name">Brine Run</span>
    </div>
    <p class="website">www.brinerunsupply.com.au</p>
  </section>

  <section class="card card-front" aria-label="Card front">
    <div class="brand">
      <span class="brand-dot"></span>
      <span class="brand-name">Brine Run</span>
    </div>
    <div class="person">
      <p class="person-name">Marcus Hale</p>
      <p class="person-role">CEO</p>
    </div>
    <div class="rule rule-top"></div>
    <p class="front-website">www.brinerunsupply.com.au</p>
    <div class="rule rule-bottom"></div>
    <ul class="contact">
      <li>
        <svg viewBox="0 0 16 16" aria-hidden="true"><path d="M4 1h3l1 4-2 1.5c.8 1.8 2 3 3.5 3.5L11 8l4 1v3c0 1-1 2-2 2C7 14 2 9 2 3c0-1 1-2 2-2z"/></svg>
        <span>0412558730</span>
      </li>
      <li>
        <svg viewBox="0 0 16 16" aria-hidden="true"><path d="M8 1a7 7 0 1 0 0 14A7 7 0 0 0 8 1zm0 1.5c.8 0 1.8 1.7 2.1 4.5H5.9C6.2 4.2 7.2 2.5 8 2.5zM2.6 7h1.8c.1-1.6.4-3 .9-3.9A5.5 5.5 0 0 0 2.6 7zm0 2a5.5 5.5 0 0 0 2.7 3.9c-.5-.9-.8-2.3-.9-3.9H2.6zm3.3 0c.3 2.8 1.3 4.5 2.1 4.5s1.8-1.7 2.1-4.5H5.9zm5.7 0c-.1 1.6-.4 3-.9 3.9A5.5 5.5 0 0 0 13.4 9h-1.8zm1.8-2a5.5 5.5 0 0 0-2.7-3.9c.5.9.8 2.3.9 3.9h1.8z"/></svg>
        <span>www.brinerunsupply.com.au</span>
      </li>
      <li class="abn">ABN: 52 118 306 274</li>
    </ul>
    <div class="edge"></div>
  </section>
</main>
</body>
</html>
```